Coral medical spa and wellness

Integrate existing logo and web design (colors and background) into tri fold, single card brochure and business card design. We already have a logo and an idea for our promotional material but we would like someone to bring it together for us! Coralwellnessandspa.com. We want to see what a marble background with a faded lily (as seen on our webpage) would look like on brochures and business cards.

```html
<!DOCTYPE html>
<html lang="en">
<head>
<meta charset="utf-8">
<title>Coral Medical Spa &amp; Wellness – Print Collateral</title>
<link rel="stylesheet" href="https://fonts.googleapis.com/css2?family=EB+Garamond:wght@400;500&display=swap">
<style>
:root{
  --stage:#8b8b8b;
  --gold:#c9a02f;
  --gold-soft:#dcbc5e;
  --ink:#262626;
  --ink-soft:#555;
  --rule:#8a8a8a;
  --bar:#3b3b3b;
  --marble:linear-gradient(135deg,#f5f5f4 0%,#ebebea 35%,#f7f7f6 60%,#e8e8e7 100%);
  --photo:linear-gradient(160deg,#f4f4f2 0%,#dedcd8 45%,#c9c6c1 70%,#ecebe8 100%);
}
*{box-sizing:border-box;margin:0;padding:0}
html,body{width:1200px;height:2545px;overflow:hidden}
body{background:var(--stage);font-family:"EB Garamond",Georgia,serif;color:var(--ink);position:relative}
.sheet{position:absolute;background:var(--marble);box-shadow:2px 3px 6px rgba(0,0,0,.35);overflow:hidden}
.abs{position:absolute}
.icons{display:none}

/* brand lockup */
.brand{position:absolute;display:flex;align-items:center;gap:10px;color:var(--gold);font-weight:500;line-height:1}
.brand .dot{border-radius:50%;background:var(--gold);flex:none}
.brand .name{display:block}
.brand .sub{display:block;letter-spacing:.06em;text-transform:uppercase;margin-top:4px}

/* photo placeholders */
.photo{position:absolute;background:var(--photo)}

/* service blocks */
.svc{position:absolute;border-top:1px solid var(--rule)}
.svc-title{font-size:18px;text-transform:uppercase;padding:6px 0 0 7px;line-height:1.1}
.svc-line{position:absolute;left:0;right:0;height:1px;background:var(--rule)}
.svc-line::before{content:"";position:absolute;left:0;top:-1px;height:3px;width:100px;background:var(--gold)}
.note{position:absolute;font-size:12.5px;border-left:1px solid var(--rule);padding-left:6px;line-height:14px}

/* price rows */
.rows{position:absolute}
.row{display:flex;align-items:flex-end;height:25.8px;padding-bottom:4px;font-size:12.5px;border-bottom:1px dotted #888}
.row:last-child{border-bottom:none}
.row.tall{height:40px}
.row span:first-child{width:135px}
.row span:nth-child(2){width:112px}
.th{display:flex;align-items:center;height:22px;background:var(--gold);color:#fff;font-size:12.5px;padding-left:6px}
.th span{border-left:1px solid #fff;padding-left:5px}
.th span:first-child{width:129px;border:none;padding:0}
.th span:nth-child(2){width:112px}

/* peel list */
.peel{position:absolute;left:0;width:322px}
.peel h3{font-weight:400;font-size:16px;line-height:17px;text-transform:uppercase}
.peel p{font-size:12.5px;line-height:15.5px;width:200px}
.peel .price{position:absolute;right:14px;top:0;font-size:12.5px}
.sep{position:absolute;left:0;width:322px;border-top:1px dotted #888}

/* footer bars */
.footbar{position:absolute;left:0;right:0;background:var(--bar);color:#fff}

/* contact lines */
.contact{position:absolute;text-align:center;font-size:17px;line-height:1}
.circ{display:inline-flex;width:36px;height:36px;border-radius:50%;background:var(--gold);align-items:center;justify-content:center}
.ico{width:14px;height:14px;fill:currentColor}

/* IV menu */
.iv{position:absolute;width:165px;font-size:7.5px;line-height:8.5px}
.iv h4{font-weight:400;font-size:8.5px;text-transform:uppercase;display:flex;gap:6px;margin-bottom:3px}
.iv h4 b{font-weight:400;border-left:1px solid var(--rule);padding-left:3px}
.iv .cols{display:grid;grid-template-columns:1fr 1fr;gap:0 6px}
.iv li{list-style:none;position:relative;padding-left:9px;margin-bottom:2px}
.iv li::before{content:"";position:absolute;left:0;top:1px;width:6px;height:6px;border-radius:50%;background:var(--gold)}
.inj{position:absolute;width:220px;font-size:6.5px;line-height:7.5px;color:var(--ink-soft)}
.inj h4{font-weight:400;font-size:8.5px;line-height:10px;color:var(--ink);text-transform:uppercase}
.inj .p{position:absolute;right:14px;top:0;font-size:8.5px;color:var(--ink);border-left:1px solid var(--rule);padding-left:3px}

/* cards */
.card .who{position:absolute;left:34px;top:143px;font-size:17px;color:var(--gold);text-transform:uppercase;letter-spacing:.02em}
.card .who small{font-size:10px;color:var(--ink);text-transform:none}
.card .rule{position:absolute;left:34px;width:385px;height:1px;background:var(--rule)}
.card .line{position:absolute;left:34px;font-size:10.5px;display:flex;align-items:center;gap:6px}
.card .line .ico{width:9px;height:9px;fill:var(--gold)}
.card .addr{position:absolute;left:285px;top:207px;font-size:10.5px;line-height:13px}
</style>
</head>
<body>

<svg class="icons" aria-hidden="true">
  <symbol id="i-phone" viewBox="0 0 24 24"><path d="M6.6 10.8a15 15 0 0 0 6.6 6.6l2.2-2.2c.3-.3.7-.4 1-.2 1.1.4 2.3.6 3.6.6.6 0 1 .4 1 1V20c0 .6-.4 1-1 1A17 17 0 0 1 3 4c0-.6.4-1 1-1h3.5c.6 0 1 .4 1 1 0 1.3.2 2.5.6 3.6.1.3 0 .7-.2 1z"/></symbol>
  <symbol id="i-mail" viewBox="0 0 24 24"><path d="M3 5h18v14H3zm2 2v.5l7 4.5 7-4.5V7zm0 2.9V17h14V9.9l-7 4.5z"/></symbol>
  <symbol id="i-globe" viewBox="0 0 24 24"><path d="M12 2a10 10 0 1 0 0 20 10 10 0 0 0 0-20zm6.9 6h-3a15 15 0 0 0-1.3-3.9A8 8 0 0 1 18.9 8zM12 4c.8 1.2 1.5 2.5 1.9 4h-3.8c.4-1.5 1.1-2.8 1.9-4zM4.3 14a8 8 0 0 1 0-4h3.4a16 16 0 0 0 0 4zm.8 2h3a15 15 0 0 0 1.3 3.9A8 8 0 0 1 5.1 16zm3-8h-3a8 8 0 0 1 4.3-3.9C8.8 5.3 8.4 6.6 8.1 8zM12 20c-.8-1.2-1.5-2.5-1.9-4h3.8c-.4 1.5-1.1 2.8-1.9 4zm2.3-6H9.7a14 14 0 0 1 0-4h4.6a14 14 0 0 1 0 4zm.3 5.9c.6-1.2 1-2.5 1.3-3.9h3a8 8 0 0 1-4.3 3.9zm1.7-5.9a16 16 0 0 0 0-4h3.4a8 8 0 0 1 0 4z"/></symbol>
  <symbol id="i-pin" viewBox="0 0 24 24"><path d="M12 2a7 7 0 0 0-7 7c0 5.2 7 13 7 13s7-7.8 7-13a7 7 0 0 0-7-7zm0 9.5a2.5 2.5 0 1 1 0-5 2.5 2.5 0 0 1 0 5z"/></symbol>
</svg>

<!-- ============ TRI-FOLD OUTSIDE ============ -->
<section class="sheet trifold-outside" style="left:62px;top:50px;width:1088px;height:768px">
  <div class="svc" style="left:23px;top:105px;width:323px;height:40px">
    <div class="svc-title">Micro Needling Pen</div>
    <div class="svc-line" style="top:38px"></div>
  </div>
  <div class="rows" style="left:23px;top:150px;width:323px">
    <div class="row"><span>Face</span><span style="margin-left:100px">$ 250</span></div>
    <div class="row"><span>Décolletage</span><span style="margin-left:100px">$ 250</span></div>
    <div class="row"><span>Add neck</span><span style="margin-left:100px">$ 50</span></div>
    <div class="row"><span>Add PRP</span><span style="margin-left:100px">$ 150</span></div>
    <div class="row"><span>Add stem cells</span><span style="margin-left:100px">$ 200</span></div>
  </div>

  <div class="svc" style="left:23px;top:355px;width:323px;height:62px">
    <div class="svc-title" style="font-size:17px;text-transform:none;line-height:21px">PRP<br>for hair restoration</div>
    <div class="note" style="left:175px;top:30px">Book for free consultation</div>
    <div class="svc-line" style="top:59px"></div>
  </div>

  <div class="svc" style="left:23px;top:495px;width:323px;height:62px">
    <div class="svc-title">Spider Vein Treatment</div>
    <div class="abs" style="left:7px;top:30px;font-size:12.5px">Starting @ $100</div>
    <div class="note" style="left:175px;top:30px">Book for free consultation</div>
    <div class="svc-line" style="top:59px"></div>
  </div>

  <div class="brand" style="left:28px;top:655px">
    <i class="dot" style="width:26px;height:26px"></i>
    <span><span class="name" style="font-size:44px">Coral</span><span class="sub" style="font-size:12px">Medical Spa &amp; Wellness</span></span>
  </div>

  <div class="brand" style="left:433px;top:238px">
    <i class="dot" style="width:26px;height:26px"></i>
    <span><span class="name" style="font-size:46px">Coral</span><span class="sub" style="font-size:12px">Medical Spa &amp; Wellness</span></span>
  </div>

  <div class="abs" style="left:453px;top:340px;display:flex;gap:10px;color:#fff">
    <span class="circ"><svg class="ico"><use href="#i-phone"/></svg></span>
    <span class="circ"><svg class="ico"><use href="#i-mail"/></svg></span>
    <span class="circ"><svg class="ico"><use href="#i-globe"/></svg></span>
    <span class="circ"><svg class="ico"><use href="#i-pin"/></svg></span>
  </div>
  <div class="contact" style="left:338px;top:403px;width:400px">(555) 014-2277</div>
  <div class="contact" style="left:338px;top:447px;width:400px">welcome@coralwellnessandspa.com</div>
  <div class="contact" style="left:338px;top:491px;width:400px">www.coralwellnessandspa.com</div>
  <div class="contact" style="left:338px;top:534px;width:400px;line-height:21px">1420 W. Harbor Lane, Suite 12<br>Fairhaven, AZ 85390</div>

  <div class="photo" role="img" aria-label="Faded white lily with spa stones and a dish of cream on a pale leaf-shaped swirl" style="left:680px;top:120px;width:408px;height:490px;border-radius:70% 0 0 45%;opacity:.9"></div>
  <div class="brand" style="left:800px;top:42px">
    <i class="dot" style="width:24px;height:24px"></i>
    <span><span class="name" style="font-size:44px">Coral</span><span class="sub" style="font-size:12px">Medical Spa &amp; Wellness</span></span>
  </div>

  <h2 class="abs" style="left:743px;top:638px;width:330px;text-align:center;font-weight:400;font-size:30px;line-height:34px">PRIORITIZE YOUR<br>HEALTH &amp; WELLNESS</h2>
  <div class="abs" style="left:746px;top:716px;width:324px;height:24px;background:var(--gold);color:#fff;font-size:14px;letter-spacing:.2em;text-align:center;line-height:24px">www.coralwellnessandspa.com</div>
</section>

<!-- ============ TRI-FOLD INSIDE ============ -->
<section class="sheet trifold-inside" style="left:65px;top:856px;width:1085px;height:766px">
  <div class="photo" role="img" aria-label="Faint lily, spa stones and cream dish fading into the marble" style="left:360px;top:0;width:725px;height:700px;opacity:.45;border-radius:0 0 0 50%"></div>

  <div class="brand" style="left:25px;top:50px">
    <i class="dot" style="width:30px;height:30px"></i>
    <span><span class="name" style="font-size:54px">Coral</span><span class="sub" style="font-size:14px">Medical Spa &amp; Wellness</span></span>
  </div>

  <div class="svc" style="left:25px;top:182px;width:320px;height:36px">
    <div class="svc-title" style="font-size:19px">Laser Hair Removal</div>
    <div class="svc-line" style="top:34px"></div>
  </div>
  <div class="rows" style="left:25px;top:234px;width:320px">
    <div class="th"><span>WOMEN</span><span>Individual</span><span>Package of 6</span></div>
    <div class="row"><span>Forehead</span><span>$ 55</span><span>$ 297</span></div>
    <div class="row"><span>Upper Lip</span><span>$ 40</span><span>$ 216</span></div>
    <div class="row"><span>Cheeks/Sideburns</span><span>$ 65</span><span>$ 351</span></div>
    <div class="row"><span>Chin</span><span>$ 40</span><span>$ 216</span></div>
    <div class="row"><span>Neck</span><span>$ 90</span><span>$ 486</span></div>
    <div class="row"><span>Full Face</span><span>$ 150</span><span>$ 810</span></div>
    <div class="row"><span>Back of neck</span><span>$ 65</span><span>$ 351</span></div>
    <div class="row"><span>Under Arm</span><span>$ 65</span><span>$ 351</span></div>
    <div class="row"><span>Half Arm</span><span>$ 75</span><span>$ 405</span></div>
    <div class="row"><span>Full Arm</span><span>$ 150</span><span>$ 810</span></div>
    <div class="row"><span>Belly</span><span>$ 140</span><span>$ 756</span></div>
    <div class="row"><span>Bikini</span><span>$ 80</span><span>$ 432</span></div>
    <div class="row"><span>Brazilian Bikini</span><span>$ 140</span><span>$ 756</span></div>
    <div class="row"><span>Half Leg</span><span>$ 100</span><span>$ 540</span></div>
    <div class="row"><span>Full Leg</span><span>$ 175</span><span>$ 945</span></div>
    <div class="row"><span>Areola</span><span>$ 30</span><span>$ 162</span></div>
  </div>

  <div class="rows" style="left:381px;top:39px;width:322px">
    <div class="th"><span>MEN</span><span>Individual</span><span>Package of 6</span></div>
    <div class="row"><span>Full Beard</span><span>$ 150</span><span>$ 810</span></div>
    <div class="row"><span>Ears</span><span>$ 30</span><span>$ 162</span></div>
    <div class="row"><span>Upper Back</span><span>$ 80</span><span>$ 432</span></div>
    <div class="row"><span>Lower Back</span><span>$ 80</span><span>$ 432</span></div>
    <div class="row"><span>Upper Chest</span><span>$ 80</span><span>$ 432</span></div>
    <div class="row"><span>Chest/Abdomen</span><span>$ 160</span><span>$ 864</span></div>
    <div class="row"><span>Shoulders</span><span>$ 80</span><span>$ 432</span></div>
    <div class="row tall"><span>Full Back<br>with Shoulders</span><span>$ 200</span><span>$ 1080</span></div>
    <div class="row"><span>Lower Arms</span><span>$ 80</span><span>$ 432</span></div>
    <div class="row"><span>Full Arms</span><span>$ 160</span><span>$ 864</span></div>
    <div class="row"><span>Underarms</span><span>$ 75</span><span>$ 405</span></div>
    <div class="row"><span>Lower Legs</span><span>$ 120</span><span>$ 800</span></div>
    <div class="row"><span>Full legs</span><span>$ 300</span><span>$ 1620</span></div>
  </div>

  <div class="svc" style="left:381px;top:457px;width:322px;height:38px">
    <div class="svc-title" style="font-size:19px">Relaxa</div>
    <div class="note" style="left:167px;top:12px">$ 11/ PER UNIT</div>
    <div class="svc-line" style="top:36px"></div>
  </div>
  <div class="svc" style="left:381px;top:541px;width:322px;height:38px">
    <div class="svc-title" style="font-size:19px">Smoothra</div>
    <div class="note" style="left:167px;top:12px">$ 4/ PER UNIT</div>
    <div class="svc-line" style="top:36px"></div>
  </div>
  <div class="svc" style="left:381px;top:625px;width:322px;height:38px">
    <div class="svc-title" style="font-size:19px">Fillers</div>
    <div class="note" style="left:167px;top:12px">Book for free consultation</div>
    <div class="svc-line" style="top:36px"></div>
  </div>

  <div class="abs lumi-peel" style="left:743px;top:41px;width:322px;height:640px">
    <div class="svc" style="left:0;top:0;width:322px;height:36px;border-top-color:#666">
      <div class="svc-title">Lumi Peel</div>
      <div class="svc-line" style="top:34px"></div>
    </div>
    <div class="peel" style="top:58px"><h3>Lumi Peel Original</h3><p>Great, general first-time peel for all ages and skin concerns.</p><span class="price">$225</span></div>
    <div class="sep" style="top:115px"></div>
    <div class="peel" style="top:138px"><h3>Lumi Peel Advanced</h3><p>This peel penetrates deeper to combat the signs of aging, soften fine lines and wrinkles, and enhance collagen stimulation to increase cell turnover and help firm the skin.</p><span class="price">$250</span></div>
    <div class="sep" style="top:256px"></div>
    <div class="peel" style="top:280px"><h3>Lumi Peel Purify</h3><p>Helpful in treating acne. This is a multi-faceted treatment for the many triggers and symptoms of acne, from dead skin cells and excessive oiliness to clogged pores and all types of blemishes.</p><span class="price">$250</span></div>
    <div class="sep" style="top:400px"></div>
    <div class="peel" style="top:423px"><h3>Lumi Peel with<br>Clarity Tone</h3><p>Works to suppress the production of melanin while promoting rapid cell turnover for more even and bright skin tone.</p><span class="price">$265</span></div>
    <div class="sep" style="top:530px"></div>
    <div class="peel" style="top:553px"><h3>Lumi Peel Body</h3><p>Similar treatment as the Clarity Tone Peel, but uniquely formulated for the body.</p><span class="price">$375</span></div>
  </div>

  <div class="footbar" style="top:710px;height:30px;font-size:15px">
    <span class="abs" style="left:112px;top:5px;display:flex;gap:8px;align-items:center"><svg class="ico" style="fill:#fff"><use href="#i-phone"/></svg>(555) 014-2277</span>
    <span class="abs" style="left:432px;top:5px;display:flex;gap:6px;align-items:center"><svg class="ico" style="fill:#fff"><use href="#i-globe"/></svg>www.coralwellnessandspa.com</span>
    <span class="abs" style="left:747px;top:5px">1420 W. Harbor Lane, Suite 12 Fairhaven, AZ 85390</span>
  </div>
</section>

<!-- ============ SINGLE CARD BROCHURE ============ -->
<section class="sheet flyer" style="left:62px;top:1645px;width:630px;height:890px">
  <div class="photo" role="img" aria-label="White lily with spa stones and a cream dish on a pale leaf swirl" style="left:318px;top:0;width:312px;height:355px;border-radius:0 0 0 60%"></div>
  <div class="brand" style="left:28px;top:50px">
    <i class="dot" style="width:24px;height:24px"></i>
    <span><span class="name" style="font-size:44px">Coral</span><span class="sub" style="font-size:12px">Medical Spa &amp; Wellness</span></span>
  </div>
  <h2 class="abs" style="left:25px;top:188px;font-weight:400;font-size:32px;line-height:37.5px">PRIORITIZE<br>YOUR<br>HEALTH &amp;<br>WELLNESS</h2>
  <div class="svc-line" style="left:25px;right:auto;width:207px;top:346px"></div>

  <div class="svc" style="left:25px;top:385px;width:318px;height:26px">
    <div class="svc-title" style="font-size:13px;padding-top:4px">IV Therapy Options</div>
    <div class="svc-line" style="top:24px"></div>
  </div>

  <div class="iv" style="left:23px;top:430px"><h4>Normal Saline <b>$100</b></h4><div>-For rehydration</div></div>
  <div class="iv" style="left:23px;top:477px"><h4>Alleviate <b>$220</b></h4><ul class="cols"><div><li>Helps with fatigue, focus and insomnia</li><li>Calcium chloride</li></div><div><li>Magnesium</li><li>Vitamin B12</li><li>Blend of Vitamins B1, B2, B3 and B5</li></div></ul></div>
  <div class="iv" style="left:23px;top:560px"><h4>Brainstorm <b>$180</b></h4><ul class="cols"><div><li>Helps with cognition</li><li>Folic acid with B12</li></div><div><li>L-taurine</li><li>Alpha-Lipoic-Acid</li></div></ul></div>
  <div class="iv" style="left:23px;top:625px"><h4>Get Up and Go <b>$170</b></h4><ul><li>Helps increase energy levels</li><li>Amino blend</li><li>Blend of Vitamins B1, B2, B3 and B5</li></ul></div>
  <div class="iv" style="left:23px;top:708px"><h4>Reboot <b>$195</b></h4><ul class="cols"><div><li>Helps treat hangover symptoms</li><li>Anti-nausea</li></div><div><li>Blend of Vitamins B1, B2, B3 and B5</li><li>Blend of Magnesium, Zinc and Selenium</li></div></ul></div>
  <div class="iv" style="left:23px;top:790px"><h4>Immunity <b>$185</b></h4><ul class="cols"><div><li>Helps increase immune defense</li><li>Vitamin C</li></div><div><li>Blend of Vitamins B1, B2, B3 and B5</li><li>Zinc chloride</li></div></ul></div>

  <div class="iv" style="left:200px;top:430px"><h4>Inner Beauty <b>$195</b></h4><ul class="cols"><div><li>Helps fortify skin, hair and nails</li><li>Vitamin C</li></div><div><li>Blend of Vitamins B1, B2, B3 and B5</li><li>Biotin</li></div></ul></div>
  <div class="iv" style="left:200px;top:525px"><h4>Quench <b>$195</b></h4><ul class="cols"><div><li>Helps rehydrate the body</li><li>Vitamin C</li></div><div><li>Blend of Vitamins B1, B2, B3 and B5</li><li>Blend of Magnesium, Zinc and Selenium</li></div></ul></div>
  <div class="iv" style="left:200px;top:620px"><h4>Recovery and<br>Performance <b>$195</b></h4><ul class="cols"><div><li>Helps improve recovery and performance</li><li>Vitamin C</li><li>Amino blend</li></div><div><li>Blend of Vitamins B1, B2, B3 and B5</li><li>Blend of Magnesium, Zinc and Selenium</li></div></ul></div>
  <div class="iv" style="left:200px;top:740px"><h4>Signature<br>Cocktail <b>$250</b></h4><ul class="cols"><div><li>Helps boost the immune system</li><li>Magnesium chloride</li><li>Dexpanthenol</li><li>Vitamin B1</li></div><div><li>Riboflavin</li><li>Vitamin B6</li><li>Vitamin B12</li><li>Calcium gluconate</li><li>Vitamin C</li></div></ul></div>

  <div class="abs" style="left:373px;top:380px;width:1px;height:455px;background:var(--gold)"></div>

  <div class="svc" style="left:388px;top:385px;width:225px;height:26px">
    <div class="svc-title" style="font-size:13px;padding-top:4px">Injectables</div>
    <div class="svc-line" style="top:24px"></div>
  </div>
  <div class="inj" style="left:388px;top:428px"><h4>Vitamin B12 Injection</h4>May improve energy levels<span class="p">$30</span></div>
  <div class="inj" style="left:388px;top:467px"><h4>MICC Injection</h4>Methionine, inositol, choline and B12. Helps convert fats to energy and may aid weight loss.<span class="p">$30</span></div>
  <div class="inj" style="left:388px;top:531px"><h4>Amino Blend Injection</h4>Glutamine, arginine, lysine and carnitine. May boost metabolism and energy levels.<span class="p">$30</span></div>
  <div class="inj" style="left:388px;top:589px"><h4>Vitamin B Complex Injection</h4>May relieve stress and improve cognitive function.<span class="p">$30</span></div>
  <div class="inj" style="left:388px;top:636px"><h4>Glutathione Injection</h4>Powerful antioxidant<span class="p">$30</span></div>
  <div class="inj" style="left:388px;top:677px"><h4>Tri-Immune Boost Injection</h4>Mix of glutathione, vitamin C and zinc. May improve immune defense.<span class="p">$40</span></div>

  <div class="abs" style="left:392px;top:725px;width:218px;height:107px;border:1px dashed #777;font-size:10px">
    <div class="abs" style="left:22px;top:16px;display:flex;gap:6px;align-items:center"><span class="circ" style="width:16px;height:16px;color:#fff"><svg class="ico" style="width:9px;height:9px"><use href="#i-phone"/></svg></span>(555) 014-2277</div>
    <div class="abs" style="left:22px;top:42px;display:flex;gap:6px;align-items:center"><span class="circ" style="width:16px;height:16px;color:#fff"><svg class="ico" style="width:9px;height:9px"><use href="#i-mail"/></svg></span>welcome@coralwellnessandspa.com</div>
    <div class="abs" style="left:22px;top:68px;display:flex;gap:6px;align-items:center"><span class="circ" style="width:16px;height:16px;color:#fff"><svg class="ico" style="width:9px;height:9px"><use href="#i-globe"/></svg></span>www.coralwellnessandspa.com</div>
  </div>

  <div class="footbar" style="top:847px;height:28px;font-size:13px;letter-spacing:.22em;text-align:center;line-height:28px">1420 W. HARBOR LANE, SUITE 12 &nbsp;FAIRHAVEN, AZ 85390</div>
</section>

<!-- ============ BUSINESS CARDS ============ -->
<section class="sheet card" style="left:703px;top:1705px;width:452px;height:257px">
  <div class="brand" style="left:35px;top:28px;gap:5px">
    <i class="dot" style="width:12px;height:12px"></i>
    <span><span class="name" style="font-size:22px">Coral</span><span class="sub" style="font-size:6px;margin-top:2px">Medical Spa &amp; Wellness</span></span>
  </div>
  <div class="who">Elena Marlow, <small>FNP-C</small></div>
  <div class="rule" style="top:170px"></div>
  <div class="line" style="top:185px"><svg class="ico"><use href="#i-phone"/></svg>(555) 014-2277</div>
  <div class="line" style="top:203px"><svg class="ico"><use href="#i-mail"/></svg>welcome@coralwellnessandspa.com</div>
  <div class="line" style="top:221px"><svg class="ico"><use href="#i-globe"/></svg>www.coralwellnessandspa.com</div>
  <div class="addr">1420 W. Harbor Lane, Suite 12<br>Fairhaven, AZ 85390</div>
</section>

<section class="sheet card" style="left:703px;top:1976px;width:452px;height:258px">
  <div class="brand" style="left:35px;top:28px;gap:5px">
    <i class="dot" style="width:12px;height:12px"></i>
    <span><span class="name" style="font-size:22px">Coral</span><span class="sub" style="font-size:6px;margin-top:2px">Medical Spa &amp; Wellness</span></span>
  </div>
  <div class="who">Rachel Torrin, <small>FNP-C</small></div>
  <div class="rule" style="top:170px"></div>
  <div class="line" style="top:185px"><svg class="ico"><use href="#i-phone"/></svg>(555) 014-2277</div>
  <div class="line" style="top:203px"><svg class="ico"><use href="#i-mail"/></svg>welcome@coralwellnessandspa.com</div>
  <div class="line" style="top:221px"><svg class="ico"><use href="#i-globe"/></svg>www.coralwellnessandspa.com</div>
  <div class="addr">1420 W. Harbor Lane, Suite 12<br>Fairhaven, AZ 85390</div>
</section>

<section class="sheet card" style="left:703px;top:2250px;width:452px;height:258px">
  <div class="brand" style="left:120px;top:85px">
    <i class="dot" style="width:24px;height:24px"></i>
    <span><span class="name" style="font-size:44px">Coral</span><span class="sub" style="font-size:12px">Medical Spa &amp; Wellness</span></span>
  </div>
  <div class="rule" style="top:205px"></div>
  <div class="abs" style="left:34px;top:204px;width:70px;height:2px;background:var(--gold)"></div>
  <div class="line" style="top:212px">www.coralwellnessandspa.com</div>
</section>

</body>
</html>
```